Digital Medical Care Start-up: New Web Design Needed

We are a startup in Boston, USA. Our current website has mostly acceptable content but looks outdated and it is ineffective. Viewers - especially possible investors - are turned off. It may also have too much content - especially the table. Current site Https://CareLoomKits.com

Business: we produce apps for surgeons to give their patients. The apps describe the medical procedure they will have, how to prepare, what to do to speed recovery, and how to interpret any symptoms. One app for each medical procedure - there are over 200.

LIKES
https://www.kestrivamed.com/
https://www.fenworthclinix.com/en/
https://zorandi.com/about/
DISLIKES
https://plax-ora.com/
https://www.tundravita.com/
https://www.grelvin-clinic.net/
https://www.quessa.com/

Target Market(s)

Audience: Medical Surgeons (customers) and Investors (we will do our first capital raise afterward the new website) in USA.

Coding

Number of Pages Required

Font styles to use
Other font styles liked:
• Candara

Colors
0455a3
f37122

Requirements
Must have
• OUTPUT:
We want a fully Responsive Version.
We do not use Wordpress. The page layout (or template) should be html + css + images + a little JavaScript.
The first page is the landing page. The second page would be the template on which we put the remaining content.
After delivery, the html would be merged into the existing framework. The site needs to be built on a template so it can be managed by an average quasi-tech person, without the need for a coder.

See exisiting company and product logos. They will remain unchanged, so make sure the website is compatable with the current logos.
Nice to have
• We have attached an idea of ours. This is meant for your stimulation, not necessarily for replication. Our attachment does not have all the content details, but the outline is correct.

```html
<!DOCTYPE html>
<html lang="en">
<head>
<meta charset="utf-8">
<title>CareLoom Kits — Digitally Delivering Procedure E-Care</title>
<link href="https://fonts.googleapis.com/css2?family=Open+Sans:wght@600;700&family=Rambla:wght@400;700&display=swap" rel="stylesheet">
<style>
  :root {
    --canvas: #e6e6e6;
    --header-bg: #f0f0fa;
    --ink: #333333;
    --nav-active: #2b7ab0;
    --brand-mark: #1b8fc2;
    --band-top: #2d84ad;
    --band-bottom: #1d6890;
    --band-rule: rgba(255,255,255,0.35);
    --white: #ffffff;
    --footer-bg: #2d2d2d;
    --footer-ink: #a9a9a9;
    --social: #8c8c8c;
  }
  * { box-sizing: border-box; margin: 0; padding: 0; }
  html, body { width: 1200px; height: 1007px; overflow: hidden; }
  body { background: var(--canvas); font-family: "Rambla", "Candara", sans-serif; }

  .page {
    position: absolute; left: 14px; top: 14px;
    width: 1172px; height: 978px;
    background: var(--white);
    overflow: hidden;
  }

  .site-header {
    position: absolute; left: 0; top: 0; width: 100%; height: 124px;
    background: var(--header-bg);
  }
  .brand {
    position: absolute; left: 22px; top: 46px;
    display: flex; align-items: center; gap: 16px;
  }
  .brand-mark { width: 48px; height: 48px; border-radius: 50%; background: var(--brand-mark); }
  .brand-name {
    font-family: "Rambla", sans-serif; font-weight: 700; font-size: 29px;
    color: var(--ink); letter-spacing: 0.5px;
  }
  .main-nav {
    position: absolute; right: 29px; top: 70px;
    display: flex; gap: 17px;
    font-family: "Open Sans", sans-serif; font-weight: 600; font-size: 14px;
    text-transform: uppercase; color: var(--ink);
  }
  .main-nav .is-active { color: var(--nav-active); }

  .hero {
    position: absolute; left: 0; top: 124px; width: 100%; height: 586px;
  }
  .hero-photo {
    position: absolute; inset: 0;
    background:
      radial-gradient(ellipse at 55% 75%, rgba(206,170,150,0.55) 0%, rgba(206,170,150,0) 40%),
      radial-gradient(ellipse at 90% 80%, rgba(235,235,235,0.7) 0%, rgba(235,235,235,0) 35%),
      linear-gradient(180deg, #3d2a63 0%, #2c2c30 20%, #55575c 55%, #6e5545 100%);
  }
  .hero-title {
    position: absolute; left: 0; right: 0; top: 266px;
    text-align: center; color: var(--white);
    font-family: "Open Sans", sans-serif; font-weight: 700; font-size: 29px;
    text-transform: uppercase; letter-spacing: 0.3px;
    text-shadow: 0 1px 3px rgba(0,0,0,0.4);
  }

  .feature-band {
    position: absolute; left: 0; top: 710px; width: 100%; height: 231px;
    background: linear-gradient(180deg, var(--band-top), var(--band-bottom));
    box-shadow: inset 0 6px 8px -6px rgba(0,0,0,0.5);
  }
  .feature {
    position: absolute; top: 50px; width: 310px; color: var(--white);
  }
  .feature:nth-child(1) { left: 39px; }
  .feature:nth-child(2) { left: 436px; }
  .feature:nth-child(3) { left: 833px; }
  .feature-title { font-size: 21px; font-weight: 400; line-height: 1.1; margin-bottom: 1px; }
  .feature-text { font-size: 13.2px; font-weight: 700; line-height: 17.5px; }
  .feature-link { position: absolute; top: 135px; left: 0; width: 28px; height: 28px; }
  .band-rule {
    position: absolute; top: 47px; width: 1px; height: 138px; background: var(--band-rule);
  }

  .site-footer {
    position: absolute; left: 0; top: 941px; width: 100%; height: 37px;
    background: var(--footer-bg);
  }
  .copyright {
    position: absolute; left: 16px; top: 9px;
    font-size: 13px; color: var(--footer-ink);
  }
  .social { position: absolute; right: 14px; top: 8px; display: flex; gap: 5px; }
  .social span { width: 21px; height: 21px; border-radius: 50%; background: var(--social); }
</style>
</head>
<body>
  <div class="page">
    <header class="site-header">
      <div class="brand">
        <span class="brand-mark"></span>
        <span class="brand-name">CARELOOMKITS</span>
      </div>
      <nav class="main-nav">
        <span class="is-active">Home</span>
        <span>About</span>
        <span>Medical Advisory Board</span>
        <span>Clinical Groups</span>
        <span>Testimonials</span>
        <span>Contact</span>
      </nav>
    </header>

    <section class="hero">
      <div class="hero-photo" role="img" aria-label="Photo of hands typing on a laptop keyboard with a team chat app on screen"></div>
      <h1 class="hero-title">Digitally Delivering Procedure E-Care</h1>
    </section>

    <section class="feature-band">
      <article class="feature">
        <h2 class="feature-title">About Us</h2>
        <p class="feature-text">Lorem ipsum dolor sit amet, consectetuer adipiscing elit, sed diam nonummy nibh euismod tincidunt ut laoreet dolore magna aliquam erat volutpat. Ut wisi enim ad minim veniam, quis nostrud exerci tation.</p>
        <svg class="feature-link" viewBox="0 0 28 28" aria-label="Read more"><circle cx="14" cy="14" r="12" fill="none" stroke="#fff" stroke-width="2"/><path d="M8 14h11M15 9.5l4.5 4.5-4.5 4.5" fill="none" stroke="#fff" stroke-width="2.2" stroke-linecap="round" stroke-linejoin="round"/></svg>
      </article>
      <article class="feature">
        <h2 class="feature-title">Services</h2>
        <p class="feature-text">Lorem ipsum dolor sit amet, consectetuer adipiscing elit, sed diam nonummy nibh euismod tincidunt ut laoreet dolore magna aliquam erat volutpat. Ut wisi enim ad minim veniam, quis nostrud exerci tation.</p>
        <svg class="feature-link" viewBox="0 0 28 28" aria-label="Read more"><circle cx="14" cy="14" r="12" fill="none" stroke="#fff" stroke-width="2"/><path d="M8 14h11M15 9.5l4.5 4.5-4.5 4.5" fill="none" stroke="#fff" stroke-width="2.2" stroke-linecap="round" stroke-linejoin="round"/></svg>
      </article>
      <article class="feature">
        <h2 class="feature-title">Latest Blog</h2>
        <p class="feature-text">Lorem ipsum dolor sit amet, consectetuer adipiscing elit, sed diam nonummy nibh euismod tincidunt ut laoreet dolore magna aliquam erat volutpat. Ut wisi enim ad minim veniam, quis nostrud exerci tation.</p>
        <svg class="feature-link" viewBox="0 0 28 28" aria-label="Read more"><circle cx="14" cy="14" r="12" fill="none" stroke="#fff" stroke-width="2"/><path d="M8 14h11M15 9.5l4.5 4.5-4.5 4.5" fill="none" stroke="#fff" stroke-width="2.2" stroke-linecap="round" stroke-linejoin="round"/></svg>
      </article>
      <span class="band-rule" style="left:388px"></span>
      <span class="band-rule" style="left:785px"></span>
    </section>

    <footer class="site-footer">
      <p class="copyright">© 2021 CareLoom Kits All Rights Reserved.</p>
      <div class="social" aria-label="Social links">
        <span></span><span></span><span></span><span></span>
      </div>
    </footer>
  </div>
</body>
</html>
```